Design a Flat design copy of this flyer

Copy the brochure but use flat design instead of 3D.
Copy placement of items.

Winning designer will be awarded website development work for word press site.

```html
<!DOCTYPE html>
<html lang="en">
<head>
<meta charset="utf-8">
<title>Sky Life – Flyer</title>
<link href="https://fonts.googleapis.com/css2?family=Arimo:wght@400;700&display=swap" rel="stylesheet">
<style>
  :root {
    --page: #ffffff;
    --sky-top: #3f67a8;
    --sky-mid: #7f9fcf;
    --sky-light: #c9d6ea;
    --navy: #1d3160;
    --navy-soft: rgba(24, 40, 82, 0.82);
    --panel: rgba(255, 255, 255, 0.94);
    --glass: rgba(235, 240, 248, 0.82);
    --grey-text: #6b6b6b;
    --dark-text: #555555;
    --tick: #3aa935;
    --opt-green: #8fd14f;
    --opt-bg: #4d4d4d;
    --band: #3b3b3b;
    --white: #ffffff;
    --api-red: #e8432d;
    --ring-blue: #2a9fd8;
    --ring-purple: #7d3a7d;
    --ring-green: #8cc63f;
    --ring-yellow: #f2c200;
    --ring-pink: #d8237a;
  }
  * { box-sizing: border-box; margin: 0; padding: 0; }
  html, body { width: 1200px; height: 870px; overflow: hidden; background: var(--page); }
  body { font-family: "Arimo", Arial, sans-serif; position: relative; }

  .flyer { position: absolute; left: 30px; top: 25px; width: 1140px; height: 810px; overflow: hidden; }
  .sky {
    position: absolute; inset: 0 0 102px 0;
    background: radial-gradient(ellipse at 35% 35%, var(--sky-light) 0%, var(--sky-mid) 40%, var(--sky-top) 85%);
  }
  .footer-band {
    position: absolute; left: 0; right: 0; bottom: 0; height: 102px; background: var(--band);
    color: var(--white); text-align: center; font-weight: 700; font-size: 20px; line-height: 25px; padding-top: 17px;
  }

  .brand {
    position: absolute; left: 44px; top: 55px; width: 78px; height: 76px; background: var(--navy);
    color: var(--white); font-weight: 700; font-size: 24px; display: flex; align-items: center; justify-content: center;
  }

  .top-nav {
    position: absolute; left: 318px; top: 60px; width: 780px; height: 47px; background: var(--glass);
    border-radius: 10px; display: flex; align-items: center;
  }
  .top-nav span { flex: 1; text-align: center; color: var(--grey-text); font-size: 20px; border-right: 2px solid #8c8c8c; line-height: 30px; }
  .top-nav span:last-child { border-right: none; flex: 1.3; }
  .top-nav span:nth-child(3) { flex: 1.5; }

  .opt-in { position: absolute; left: 927px; top: 138px; width: 171px; height: 51px; background: var(--glass); border-radius: 8px; }
  .opt-in b {
    position: absolute; right: 4px; top: 4px; width: 93px; height: 43px; background: var(--opt-bg); border-radius: 6px;
    color: var(--opt-green); font-size: 20px; display: flex; align-items: center; justify-content: center;
  }

  .feature { position: absolute; height: 52px; }
  .feature .ring {
    position: absolute; left: 0; top: 0; width: 52px; height: 52px; border-radius: 50%; background: var(--white);
    border: 4px solid; display: flex; align-items: center; justify-content: center; box-shadow: 0 0 0 2px #dfe6f1 inset;
  }
  .feature .ring svg { width: 28px; height: 28px; }
  .feature .tab {
    position: absolute; left: 62px; top: 6px; width: 220px; height: 41px; background: var(--navy-soft);
    clip-path: polygon(20px 0, 100% 0, 100% 100%, 20px 100%, 0 50%);
    color: var(--white); font-weight: 700; font-size: 16px; display: flex; align-items: center; justify-content: center; padding-left: 14px;
  }
  .feature .tab em { color: var(--api-red); font-style: normal; }
  .blue { border-color: var(--ring-blue) !important; }
  .purple { border-color: var(--ring-purple) !important; }
  .green { border-color: var(--ring-green) !important; }
  .yellow { border-color: var(--ring-yellow) !important; }
  .pink { border-color: var(--ring-pink) !important; }

  .callout { position: absolute; background: var(--panel); border-radius: 10px; color: var(--grey-text); font-weight: 700; }
  .callout ul { list-style: none; }
  .callout li { display: flex; align-items: center; gap: 6px; font-size: 18px; line-height: 28px; }
  .callout li svg { width: 18px; height: 16px; flex: none; }
  .offer { left: 725px; top: 223px; width: 373px; height: 194px; padding: 14px 0 0 16px; }
  .offer h2 { font-size: 22px; line-height: 26px; margin: 0 0 4px 5px; color: var(--dark-text); }
  .offer ul { margin-top: 2px; }
  .benefits { left: 244px; top: 535px; width: 418px; height: 154px; padding: 8px 0 0 10px; }
  .benefits::after {
    content: ""; position: absolute; right: -18px; top: 26px; border: 18px solid transparent; border-left-color: var(--panel); border-right: 0;
  }

  .community { position: absolute; left: 42px; top: 535px; width: 138px; height: 132px; border-radius: 50%;
    background: radial-gradient(circle, transparent 30%, #f2a33a 31%, #e33d3d 60%, #4a90d9 100%); opacity: .9; }
  .community-label { position: absolute; left: 40px; top: 672px; font-size: 16px; font-weight: 700; color: #111; }

  .figure { position: absolute; background: linear-gradient(160deg, #3a3a3a, #050505); border-radius: 40px 40px 8px 8px; }
  .figure-left { left: 680px; top: 408px; width: 150px; height: 262px; }
  .figure-right { left: 900px; top: 418px; width: 150px; height: 200px; }

  .product-name {
    position: absolute; left: 758px; top: 525px; width: 310px; height: 155px; background: #c6c6c6; border-radius: 12px;
    color: #4e4e4e; font-weight: 700; font-size: 80px; line-height: 72px; padding: 8px 0 0 12px;
  }
  .product-name span { display: block; }
  .product-name span + span { padding-left: 150px; }
</style>
</head>
<body>
<div class="flyer">
  <div class="sky" role="img" aria-label="Blue sky with white clouds behind a fine diagonal line texture"></div>

  <div class="brand">BFS.</div>

  <nav class="top-nav">
    <span>Privacy</span><span>Security</span><span>Multiple Languages</span><span>Personalisation</span>
  </nav>

  <div class="opt-in"><b>Opt In</b></div>

  <!-- left column -->
  <div class="feature" style="left:44px;top:171px">
    <div class="ring blue"><svg viewBox="0 0 28 28"><circle cx="10" cy="9" r="5" fill="#777"/><circle cx="18" cy="9" r="5" fill="#555"/><path d="M2 25c0-7 16-7 16 0zM10 25c0-7 16-7 16 0z" fill="#666"/></svg></div>
    <div class="tab">Friends, Family, Contacts</div>
  </div>
  <div class="feature" style="left:44px;top:243px">
    <div class="ring blue"><svg viewBox="0 0 28 28"><path d="M14 3 2 14h4v11h16V14h4z" fill="#555"/></svg></div>
    <div class="tab">Properties</div>
  </div>
  <div class="feature" style="left:44px;top:313px">
    <div class="ring purple"><svg viewBox="0 0 28 28"><path d="M14 3 2 14h4v11h16V14h4z" fill="#555"/><path d="M16 15l-4 5h3l-2 4 5-6h-3z" fill="#f2c200"/></svg></div>
    <div class="tab">Utilities</div>
  </div>
  <div class="feature" style="left:44px;top:386px">
    <div class="ring green"><svg viewBox="0 0 28 28"><path d="M2 14a12 10 0 0 1 24 0z" fill="#555"/><path d="M14 14v9a2 2 0 0 1-4 0" stroke="#555" stroke-width="2" fill="none"/></svg></div>
    <div class="tab">Insurances</div>
  </div>
  <div class="feature" style="left:44px;top:457px">
    <div class="ring yellow"><svg viewBox="0 0 28 28"><path d="M4 14l3-7h14l3 7v8H4z" fill="#555"/><circle cx="8" cy="18" r="2" fill="#fff"/><circle cx="20" cy="18" r="2" fill="#fff"/></svg></div>
    <div class="tab">Vehicles</div>
  </div>

  <!-- right column -->
  <div class="feature" style="left:398px;top:171px">
    <div class="ring yellow"><svg viewBox="0 0 28 28"><rect x="3" y="7" width="22" height="14" rx="2" fill="#555"/><rect x="3" y="10" width="22" height="3" fill="#ccc"/></svg></div>
    <div class="tab">Financial</div>
  </div>
  <div class="feature" style="left:398px;top:243px">
    <div class="ring pink"><svg viewBox="0 0 28 28"><path d="M14 2l2 9 10 5v2l-10-2-1 6 3 2v2l-4-1-4 1v-2l3-2-1-6-10 2v-2l10-5z" fill="#555"/></svg></div>
    <div class="tab">Travel</div>
  </div>
  <div class="feature" style="left:398px;top:313px">
    <div class="ring pink"><svg viewBox="0 0 28 28"><path d="M14 25 3 14a6 6 0 0 1 11-8 6 6 0 0 1 11 8z" fill="#d8237a"/><path d="M4 14h6l2-4 3 8 2-4h7" stroke="#fff" stroke-width="1.6" fill="none"/></svg></div>
    <div class="tab">Biometrics</div>
  </div>
  <div class="feature" style="left:398px;top:386px">
    <div class="ring green"><svg viewBox="0 0 28 28"><ellipse cx="11" cy="11" rx="9" ry="7" fill="#555"/><ellipse cx="18" cy="17" rx="8" ry="6" fill="#999"/></svg></div>
    <div class="tab">Notification</div>
  </div>
  <div class="feature" style="left:398px;top:457px">
    <div class="ring yellow"><svg viewBox="0 0 28 28"><path d="M3 14h8M11 9h6v10h-6zM17 11h5M17 17h5" stroke="#555" stroke-width="2.4" fill="none"/></svg></div>
    <div class="tab"><em>API</em>&nbsp;Designer / Plugin</div>
  </div>

  <section class="callout offer">
    <h2>Offering users:</h2>
    <ul>
      <li><svg viewBox="0 0 18 16"><path d="M1 9l5 5L17 2" stroke="var(--tick)" stroke-width="3" fill="none"/></svg>Transparent Opt in Process</li>
      <li><svg viewBox="0 0 18 16"><path d="M1 9l5 5L17 2" stroke="var(--tick)" stroke-width="3" fill="none"/></svg>Smart Search</li>
      <li><svg viewBox="0 0 18 16"><path d="M1 9l5 5L17 2" stroke="var(--tick)" stroke-width="3" fill="none"/></svg>Organise and link your personal data</li>
      <li><svg viewBox="0 0 18 16"><path d="M1 9l5 5L17 2" stroke="var(--tick)" stroke-width="3" fill="none"/></svg>Left &amp; Right hand Smart Interface</li>
      <li><svg viewBox="0 0 18 16"><path d="M1 9l5 5L17 2" stroke="var(--tick)" stroke-width="3" fill="none"/></svg>Buying Power</li>
    </ul>
  </section>

  <section class="callout benefits">
    <ul>
      <li><svg viewBox="0 0 18 16"><path d="M1 9l5 5L17 2" stroke="var(--tick)" stroke-width="3" fill="none"/></svg>Establish your needs, wants &amp; wishes</li>
      <li><svg viewBox="0 0 18 16"><path d="M1 9l5 5L17 2" stroke="var(--tick)" stroke-width="3" fill="none"/></svg>Make your money go further</li>
      <li><svg viewBox="0 0 18 16"><path d="M1 9l5 5L17 2" stroke="var(--tick)" stroke-width="3" fill="none"/></svg>User ranked product suppliers</li>
      <li><svg viewBox="0 0 18 16"><path d="M1 9l5 5L17 2" stroke="var(--tick)" stroke-width="3" fill="none"/></svg>Providing the tools you need</li>
      <li><svg viewBox="0 0 18 16"><path d="M1 9l5 5L17 2" stroke="var(--tick)" stroke-width="3" fill="none"/></svg>Smart Recommendations specified by you</li>
    </ul>
  </section>

  <div class="community" role="img" aria-label="Colourful ring of figures joining hands, symbolising the sharing economy"></div>
  <div class="community-label">Sharing Economy</div>

  <div class="figure figure-left" role="img" aria-label="Black stick figure leaning on the product name sign"></div>
  <div class="figure figure-right" role="img" aria-label="Black stick figure holding up the product name sign"></div>
  <div class="product-name"><span>Sky</span><span>Life</span></div>

  <footer class="footer-band">
    T:&nbsp; +44 (0) 20 7946 0321<br>
    www.brightfieldsystems.com
  </footer>
</div>
</body>
</html>
```